Patient Fact sheets for medical conditions and treatments

Hi,

I need a new design for my patient fact sheets. I am moving from my current clinic and I am looking from a new look.

I have attached
1. a current Fact sheet
2. New home page to the website
3. New Logo.

They need to be single page and easily readable for patients.

The will be in both PDF and print form in the future.

Target Market(s)

Patients with chronic pain age 40+

Font styles to use
Serif

Requirements
Must have
• My logo, should be inline with design elements on the Front page provided.

Please use the same font as the Logo

```html
<!DOCTYPE html>
<html lang="en">
<head>
<meta charset="utf-8">
<title>Fact Sheets – PRP</title>
<link rel="stylesheet" href="https://fonts.googleapis.com/css2?family=Oswald:wght@600&family=Bebas+Neue&family=Open+Sans:wght@400;600;700&display=swap">
<style>
:root{
  --bg:#4a4a4a;
  --paper:#ffffff;
  --purple:#4b2a8e;
  --purple-deep:#2c1764;
  --purple-mid:#3b2178;
  --navy:#1e1645;
  --blue:#4a80c8;
  --ink:#2b2b2b;
  --photo-a:#e9e9e9;
  --photo-b:#7d7d7d;
}
*{margin:0;padding:0;box-sizing:border-box}
html,body{width:1200px;height:1000px;overflow:hidden;background:var(--bg)}
.sheet{position:absolute;left:285px;top:57px;width:623px;height:882px;background:var(--paper);overflow:hidden;font-family:"Open Sans",sans-serif;color:var(--ink)}
.header-art{position:absolute;left:0;top:0}
.logo{position:absolute;left:36px;top:52px;display:flex;align-items:center;white-space:nowrap}
.logo-mark{width:16px;height:16px;background:var(--navy);margin-right:12px;flex:none}
.logo-name{font-family:"Open Sans",sans-serif;font-weight:600;font-size:26px;line-height:30px;color:var(--navy);letter-spacing:.5px}
.title-band{position:absolute;left:34px;top:130px;font-family:"Oswald",sans-serif;font-weight:600;font-size:44px;color:#fff;letter-spacing:.5px}
.heading{position:absolute;font-weight:700;color:var(--navy);font-size:17px;line-height:20px;letter-spacing:.2px}
.heading.light{color:#fff}
.rule{position:absolute;height:1px;background:var(--navy)}
.rule::before{content:"";position:absolute;left:0;top:-2px;width:95px;height:4px;background:var(--navy)}
.rule.on-dark{background:#fff}
.rule.on-dark::before{background:#fff}
.copy{position:absolute;font-size:8.6px;line-height:11.9px;text-align:justify}
.copy p{margin-bottom:4px}
.copy strong{font-weight:700;color:#111}
.col-divider{position:absolute;left:313px;top:218px;width:2px;height:570px;background:#cfcfcf}
.ticks{position:absolute;left:340px;top:217px;width:247px;list-style:none;font-size:8.6px;line-height:11.9px}
.ticks li{position:relative;padding-left:29px;margin-bottom:4px}
.ticks svg{position:absolute;left:0;top:1px}
.treat-panel{position:absolute;left:340px;top:343px;width:283px;height:284px;background:var(--purple)}
.treat-panel .lower{position:absolute;left:0;top:82px;width:283px;height:202px;background:linear-gradient(180deg,var(--purple-mid),var(--purple))}
.treat-sub{position:absolute;left:22px;top:58px;color:#fff;font-weight:700;font-size:11.5px}
.treat-list{position:absolute;left:20px;top:92px;width:260px;list-style:none;display:grid;grid-template-columns:142px 118px;row-gap:11px}
.treat-list li{display:flex;align-items:center;height:26px;color:#fff;font-weight:700;font-size:10.5px;line-height:11.5px}
.treat-list .dot{width:26px;height:26px;border-radius:50%;background:#fff;flex:none;margin-right:10px}
.footer-art{position:absolute;left:0;top:790px}
.contact{position:absolute;left:34px;list-style:none;color:#fff;font-size:10.5px;line-height:13px}
.contact li{position:absolute;left:0;display:flex;white-space:nowrap}
.contact .ico{width:13px;height:13px;border-radius:2px;background:var(--blue);margin-right:10px;flex:none;margin-top:1px;display:flex;align-items:center;justify-content:center}
.social{display:inline-block;width:14px;height:14px;background:var(--blue);margin-left:4px;vertical-align:-3px}
.phone{position:absolute;top:836px;font-family:"Bebas Neue",sans-serif;font-size:25px;line-height:26px;color:#fff;display:flex;align-items:center;letter-spacing:.2px;white-space:nowrap}
.phone svg{margin-right:9px}
</style>
</head>
<body>
<main class="sheet">
  <svg class="header-art" width="623" height="200" viewBox="0 0 623 200">
    <defs>
      <linearGradient id="photoTone" x1="0" y1="0" x2="1" y2="1">
        <stop offset="0" stop-color="var(--photo-a)"/>
        <stop offset="1" stop-color="var(--photo-b)"/>
      </linearGradient>
      <linearGradient id="bandTone" x1="0" y1="0" x2="0" y2="1">
        <stop offset="0" stop-color="#55329a"/>
        <stop offset="1" stop-color="var(--purple-deep)"/>
      </linearGradient>
    </defs>
    <g role="img" aria-label="Black and white photograph of a gloved hand filling blood sample tubes in a rack">
      <polygon points="380,0 623,0 623,199 285,199" fill="url(#photoTone)"/>
    </g>
    <polygon points="370,0 380,0 285,199 273,199" fill="var(--blue)"/>
    <polygon points="0,116 330,116 290,199 0,199" fill="url(#bandTone)"/>
  </svg>
  <div class="logo"><span class="logo-mark"></span><span class="logo-name">DR RUTH ALDER</span></div>
  <div class="title-band">FACT SHEETS</div>

  <h2 class="heading" style="left:35px;top:210px">WHAT IS PRP?</h2>
  <div class="rule" style="left:35px;top:239px;width:258px"></div>
  <div class="copy" style="left:35px;top:250px;width:258px">
    <p>Platelet-Rich Plasma (PRP) is concentrated platelets and white blood cells derived from your own blood.</p>
    <p>Platelet Rich Plasma Injection Therapy (PRP therapy), is a growing treatment approach for soft tissue injuries including tendon, muscle and ligaments. It is also showing good results for mild to moderate osteoarthritis.</p>
    <p>While this approach has been used overseas for many years, it’s fairly new to Australia in the treatment of musculoskeletal and orthopaedic conditions.</p>
  </div>

  <h2 class="heading" style="left:35px;top:384px">HOW DOES PRP WORK?</h2>
  <div class="rule" style="left:35px;top:412px;width:258px"></div>
  <div class="copy" style="left:35px;top:424px;width:258px">
    <p>Some tissues in the body have a poor blood supply or respond poorly to excessive load, ultimately failing to heal naturally. While some of our primary treatment such as physiotherapy, massage, biomechanical correction and other forms of treatment are used to treat these soft tissue injuries, sometimes the body fails to respond.</p>
    <p>PRP therapy utilises the healing properties in blood to allow a healing reaction to occur in a tissue that’s not healing on its own. Our blood has small granules called ‘platelets’, which contain special growth factors that when released, allow stem cells in the particular tissue to ‘switch’ on and cause new tissue to be created and heal the injured area.</p>
    <p>Take the example of achilles tendinopathy. If the achilles is painful, thickened and not responding to rehabilitation, then the sports physician will inject the PRP into the achilles which will cause the tendon cells (tenocytes/fibroblasts) to create new achilles collagen to strengthen the achilles. White blood cells also enter the area to mop up any achilles tissue that may have been damaged due to the ongoing pain and thickening in the area.</p>
  </div>

  <h2 class="heading" style="left:37px;top:692px;font-size:18px;line-height:21px">ROLE OF PLATELETS &amp;<br>GROWTH FACTORS</h2>
  <div class="rule" style="left:37px;top:738px;width:256px"></div>
  <div class="copy" style="left:37px;top:751px;width:256px"><p><strong>PRP contains highly concentrated platelets. Platelets have been identified to secrete growth factors, which are known to play a role in:</strong></p></div>

  <div class="col-divider"></div>

  <ul class="ticks">
    <li><svg width="10" height="10" viewBox="0 0 10 10"><circle cx="5" cy="5" r="5" fill="var(--navy)"/><path d="M2.6 5.2l1.6 1.6 3.2-3.3" stroke="#fff" stroke-width="1.3" fill="none"/></svg>Increasing tissue vascularity and increasing the rate of epithelial tissue production (wound healing)</li>
    <li><svg width="10" height="10" viewBox="0 0 10 10"><circle cx="5" cy="5" r="5" fill="var(--navy)"/><path d="M2.6 5.2l1.6 1.6 3.2-3.3" stroke="#fff" stroke-width="1.3" fill="none"/></svg>Attracting other cells that fight infection</li>
    <li><svg width="10" height="10" viewBox="0 0 10 10"><circle cx="5" cy="5" r="5" fill="var(--navy)"/><path d="M2.6 5.2l1.6 1.6 3.2-3.3" stroke="#fff" stroke-width="1.3" fill="none"/></svg>Acting as a seal during closures</li>
    <li><svg width="10" height="10" viewBox="0 0 10 10"><circle cx="5" cy="5" r="5" fill="var(--navy)"/><path d="M2.6 5.2l1.6 1.6 3.2-3.3" stroke="#fff" stroke-width="1.3" fill="none"/></svg>Providing an immediate surgical hemostatic agent (reduction of bleeding)</li>
    <li><svg width="10" height="10" viewBox="0 0 10 10"><circle cx="5" cy="5" r="5" fill="var(--navy)"/><path d="M2.6 5.2l1.6 1.6 3.2-3.3" stroke="#fff" stroke-width="1.3" fill="none"/></svg>Osteogenesis (bone regeneration and repair)</li>
  </ul>

  <section class="treat-panel">
    <div class="lower"></div>
    <h2 class="heading light" style="left:22px;top:10px;font-size:18px">WHAT CAN PRP TREAT?</h2>
    <div class="rule on-dark" style="left:22px;top:39px;width:226px"></div>
    <div class="treat-sub">PRP THERAPY CAN BE USED FOR:</div>
    <ul class="treat-list">
      <li><span class="dot"></span>Orthopedic<br>surgery</li>
      <li><span class="dot"></span>Cardiac<br>surgery</li>
      <li><span class="dot"></span>Plastic and<br>cosmetic surgery</li>
      <li><span class="dot"></span>Burn care</li>
      <li><span class="dot"></span>Oral maxillofacial<br>surgery</li>
      <li><span class="dot"></span>Neurosu-<br>rgery</li>
      <li><span class="dot"></span>Ear, nose,<br>surgery</li>
      <li><span class="dot"></span>Wound<br>healing</li>
      <li><span class="dot"></span>Throat (ENT)<br>surgery</li>
      <li><span class="dot"></span>Vascular<br>surgery</li>
    </ul>
  </section>

  <h2 class="heading" style="left:349px;top:639px;font-size:19px;line-height:21px">WHAT ARE THE EXPECTED<br>RESULTS OF PRP?</h2>
  <div class="rule" style="left:349px;top:688px;width:238px"></div>
  <div class="copy" style="left:349px;top:700px;width:238px">
    <p>Because the goal of PRP therapy is to resolve pain through healing, it could prove to have lasting results. Initial improvement may be seen within a few weeks, gradually increasing as the healing progresses. Research studies and clinical practice have shown PRP therapy to be very effective at relieving pain and returning patients to their normal lives. The need for surgery can also be greatly reduced by treating injured tissues before the damage progresses and the condition is irreversible.</p>
  </div>

  <svg class="footer-art" width="623" height="92" viewBox="0 0 623 92">
    <polygon points="0,18 327,10 270,92 0,92" fill="var(--purple)"/>
    <polygon points="305,30 623,30 623,82 297,82" fill="var(--purple-deep)"/>
    <line x1="442" y1="36" x2="442" y2="76" stroke="#6a58a6" stroke-width="1"/>
  </svg>

  <ul class="contact">
    <li style="top:810px"><span class="ico"><svg width="7" height="9" viewBox="0 0 7 9"><path d="M3.5 0a3 3 0 0 1 3 3c0 2.2-3 6-3 6s-3-3.8-3-6a3 3 0 0 1 3-3z" fill="#fff"/><circle cx="3.5" cy="3" r="1.1" fill="var(--blue)"/></svg></span>Northgate Pain Group Harbour House, Ground<br>Floor 118 Linden Road Ashvale VIC 3168</li>
    <li style="top:841px"><span class="ico"><svg width="9" height="7" viewBox="0 0 9 7"><rect x=".5" y=".5" width="8" height="6" fill="none" stroke="#fff"/><path d="M.5.5l4 3.3 4-3.3" fill="none" stroke="#fff"/></svg></span>info@northgatepain.com.au</li>
    <li style="top:859px"><span class="ico"><svg width="9" height="9" viewBox="0 0 9 9"><circle cx="4.5" cy="4.5" r="3.8" fill="none" stroke="#fff"/><path d="M.7 4.5h7.6M4.5.7v7.6" stroke="#fff" stroke-width=".8"/></svg></span>www.northgatepain.com.au<span class="social" style="margin-left:9px"></span><span class="social"></span><span class="social"></span></li>
  </ul>

  <div class="phone" style="left:308px"><svg width="14" height="14" viewBox="0 0 14 14"><path d="M3 1l2.3 2.6-1.2 1.6c.9 1.9 2.3 3.3 4.2 4.2l1.6-1.2L12.5 10.6 11 12.8C6 12.3 1.8 8 1.2 3z" fill="var(--blue)"/></svg>03 9000 0142</div>
  <div class="phone" style="left:457px"><svg width="16" height="14" viewBox="0 0 16 14"><rect x="4" y="0" width="8" height="4" fill="var(--blue)"/><rect x="0" y="5" width="16" height="6" rx="1" fill="var(--blue)"/><rect x="4" y="9" width="8" height="5" fill="#fff" stroke="var(--blue)"/></svg>03 9000 0143</div>
</main>
</body>
</html>
```